Attorney Business Card

I need a business card that looks professional yet modern. I am an Attorney. , I need a professional yet modern business card for my law practice. My logo and information have been uploaded. , I need a business card that looks professional yet modern. I am an Attorney. , I need a professional yet modern business card for my law practice. My logo and information have been uploaded.

Industry/Entity Type

Business

Requirements
Must have
• My logo which has been uploaded , my logo , My logo which has been uploaded , my logo

```html
<!DOCTYPE html>
<html lang="en">
<head>
<meta charset="utf-8">
<title>Marwood Law Firm — Business Card</title>
<link rel="stylesheet" href="https://fonts.googleapis.com/css2?family=Cinzel:wght@400;600&family=Tinos:wght@400;700&display=swap">
<style>
  :root {
    --page: #ffffff;
    --navy-edge: #14344b;
    --navy-mid: #215f86;
    --ink: #1b1b1b;
    --paper: #ffffff;
  }
  * { margin: 0; padding: 0; box-sizing: border-box; }
  html, body { width: 1000px; height: 1200px; overflow: hidden; background: var(--page); }
  .canvas { position: relative; width: 1000px; height: 1200px; }

  .card {
    position: absolute; left: 129px; width: 743px; height: 425px; overflow: hidden;
    background: linear-gradient(90deg, var(--navy-edge) 0%, var(--navy-mid) 50%, var(--navy-edge) 100%);
    color: var(--paper);
  }
  .card--front { top: 152px; }
  .card--back { top: 623px; }

  .card__zigzag { position: absolute; left: 0; bottom: 0; width: 743px; height: 48px; display: block; }

  /* Front */
  .brand__circle {
    position: absolute; left: 50%; top: 42px; transform: translateX(-50%);
    width: 160px; height: 160px; border: 5px solid var(--paper); border-radius: 50%;
  }
  .brand__name {
    position: absolute; left: 0; right: 0; top: 228px; text-align: center;
    font-family: "Cinzel", serif; font-weight: 400; font-size: 76px; letter-spacing: 3px; line-height: 1;
  }
  .brand__sub {
    position: absolute; left: 0; right: 0; top: 318px; text-align: center;
    font-family: "Cinzel", serif; font-weight: 400; font-size: 34px; letter-spacing: 2px; line-height: 1;
  }

  /* Back */
  .card__header {
    position: absolute; left: 0; top: 0; width: 100%; height: 102px; background: var(--ink);
    text-align: center; font-family: "Tinos", serif; font-size: 33px; line-height: 38px; letter-spacing: 1px;
    padding-top: 10px;
  }
  .badge {
    position: absolute; left: 76px; top: 128px; width: 165px; height: 165px;
    border: 5px solid var(--paper); border-radius: 50%;
    display: flex; align-items: center; justify-content: center; text-align: center;
    font-family: "Tinos", serif; font-weight: 700; font-size: 21px; line-height: 1.2; letter-spacing: 1px;
  }
  .address {
    position: absolute; left: 270px; width: 400px; top: 132px; text-align: center;
    font-family: "Tinos", serif; font-size: 24px; line-height: 31px; letter-spacing: 1px;
  }
  .contact {
    position: absolute; top: 296px; font-family: "Tinos", serif; font-weight: 700;
    font-size: 20px; line-height: 26px; text-align: center;
  }
  .contact--web { left: 40px; width: 260px; }
  .contact--phone { left: 420px; width: 270px; }
</style>
</head>
<body>
<div class="canvas">

  <section class="card card--front" aria-label="Card front">
    <div class="brand__circle"></div>
    <div class="brand__name">MARWOOD</div>
    <div class="brand__sub">LAW FIRM</div>
    <svg class="card__zigzag" viewBox="0 0 743 48" preserveAspectRatio="none" aria-hidden="true">
      <path fill="#1b1b1b" d="M0 12 L20 4 L90 40 Q100 46 110 40 L158 4 L240 40 Q250 46 260 40 L305 4 L385 40 Q395 46 405 40 L450 4 L530 40 Q540 46 550 40 L595 4 L675 40 Q685 46 695 40 L735 8 L743 8 L743 48 L0 48 Z"/>
    </svg>
  </section>

  <section class="card card--back" aria-label="Card back">
    <header class="card__header">
      <div class="person__name">DANIEL MARWOOD, ESQ.</div>
      <div class="person__title">ATTORNEY AT LAW</div>
    </header>
    <div class="badge">MARWOOD<br>LAW FIRM</div>
    <address class="address" style="font-style:normal">
      2280 STERLING AVE.<br>PENTHOUSE<br>WESTBROOK, CA 90418<br>555.014.2200 TEL
    </address>
    <div class="contact contact--web">DANIEL@MWFIRM.COM<br>WWW.MWFIRM.COM</div>
    <div class="contact contact--phone">555.014.2201 FAX<br>555.018.3344 MOBILE</div>
    <svg class="card__zigzag" viewBox="0 0 743 48" preserveAspectRatio="none" aria-hidden="true">
      <path fill="#1b1b1b" d="M0 12 L20 4 L90 40 Q100 46 110 40 L158 4 L240 40 Q250 46 260 40 L305 4 L385 40 Q395 46 405 40 L450 4 L530 40 Q540 46 550 40 L595 4 L675 40 Q685 46 695 40 L735 8 L743 8 L743 48 L0 48 Z"/>
    </svg>
  </section>

</div>
</body>
</html>
```